Labels for new organic cosmetics/personal care brand called Verimo

I need labels for new cosmetic brand named ( Verimo )
It is natural and organic
products include:
**natural soaps 3 in a box ( 7 types): shea butter soap, almond soap, lavender soap, apricot soap, olive soap , camel milk soap and sensitive skin soap.

**Organic shea butters (7 types) (in round container) pure shea butter, Shea butter with argan oil, shea butter with olive oil, shea butter with oats, Shea butter with camel milk, shea butter with camel milk and Agarwood and shea butter with donky milk.

**deodorant: one type only , a crystal deodorant.

**shampoo (in cylindrical container) : one type natural shampoo

** Organic Oils (two types) (in clyndrical container) : Argan oil and Rose hip oil.

attached examples of similar containers and outline of labels that i want to have new ones.
**notice:
shape of shea butter container is round and flat.
shape of shampoo is cylindrical.
shape of soaps is a cuboid box.

Target Market(s)

men and women of all ages

Industry/Entity Type

Cosmetics

Font styles to use
Sans Serif

Colors
e4daeb
f9d9e8
fbd4d5
fee3d5
fce8d3
fff3d1
fdf9cf
cee9f5
cadf82

Requirements
Must have
• * Verimo logo
• * organic/natural theme
• * front and back labels
• * 7 labels for soaps, 7 back and 7 front labels for shea butter, one label for deoderant, one label for shampoo, two labels for natural oils.
Nice to have
• leaves, green colors or natural shades of colors , pastel colors
• the color is not specified
Should not have
• **I don't need the container design** .
• just the labels. attached are outline example of the labels and photos of the products so you know the shape of container.
• shape of shea butter container is round and flat.
• shape of shampoo is cylindrical.
• shape of soaps is a cuboid box.

```html
<!DOCTYPE html>
<html lang="en">
<head>
<meta charset="utf-8">
<title>Verimo Argan Oil Label</title>
<link rel="stylesheet" href="https://fonts.googleapis.com/css2?family=Josefin+Sans:wght@300;400;600;700&display=swap">
<style>
  :root {
    --backdrop: #d9d9d9;
    --label-white: #f4f4f4;
    --leaf-dark: #1d8a1f;
    --leaf-mid: #3f9e1c;
    --leaf-light: #86b81a;
    --band-green: #8fbd12;
    --band-line: #2e8f1c;
    --brand-crimson: #b5134f;
    --type-white: #ffffff;
    --fruit-amber: #d9a54a;
    --fruit-olive: #8f9a55;
  }
  html, body {
    margin: 0;
    padding: 0;
    width: 1042px;
    height: 1200px;
    overflow: hidden;
    background: var(--backdrop);
  }
  .canvas {
    position: relative;
    width: 1042px;
    height: 1200px;
  }
  .label {
    position: absolute;
    left: 241px;
    top: 80px;
    width: 560px;
    height: 1040px;
    font-family: "Josefin Sans", sans-serif;
  }
  .brand-name {
    font-family: "Josefin Sans", sans-serif;
    font-weight: 600;
    font-size: 58px;
    fill: var(--brand-crimson);
  }
  .product-word {
    font-family: "Josefin Sans", sans-serif;
    font-weight: 300;
    font-size: 62px;
    fill: var(--type-white);
    letter-spacing: 1px;
  }
  .product-type {
    font-family: "Josefin Sans", sans-serif;
    font-weight: 700;
    font-size: 190px;
    fill: var(--type-white);
  }
  .claim {
    font-family: "Josefin Sans", sans-serif;
    font-weight: 400;
    font-size: 24px;
    fill: var(--type-white);
  }
  .descriptor {
    font-family: "Josefin Sans", sans-serif;
    font-weight: 600;
    font-size: 22px;
    fill: var(--type-white);
  }
  .volume {
    font-family: "Josefin Sans", sans-serif;
    font-weight: 700;
    font-size: 28px;
    fill: var(--type-white);
  }
</style>
</head>
<body>
<main class="canvas">
  <svg class="label" viewBox="0 0 560 1040" xmlns="http://www.w3.org/2000/svg">
    <defs>
      <linearGradient id="leafGradient" x1="0" y1="0" x2="0" y2="1">
        <stop offset="0" stop-color="var(--leaf-light)"/>
        <stop offset="0.35" stop-color="var(--leaf-mid)"/>
        <stop offset="1" stop-color="var(--leaf-dark)"/>
      </linearGradient>
      <radialGradient id="fruitGradient" cx="0.5" cy="0.5" r="0.6">
        <stop offset="0" stop-color="var(--fruit-amber)"/>
        <stop offset="1" stop-color="var(--fruit-olive)"/>
      </radialGradient>
    </defs>

    <rect class="label-base" x="0" y="0" width="560" height="1040" fill="var(--label-white)"/>

    <g class="brand">
      <circle cx="178" cy="158" r="16" fill="var(--brand-crimson)"/>
      <text class="brand-name" x="208" y="178">Verimo</text>
    </g>

    <path class="leaf-panel" d="M0,240 C150,250 250,290 280,400 C310,290 410,250 560,240 L560,1040 L0,1040 Z" fill="url(#leafGradient)"/>

    <path class="oil-drop" d="M280,410 C292,432 304,446 304,462 A24,24 0 0 1 256,462 C256,446 268,432 280,410 Z" fill="var(--type-white)"/>

    <text class="product-word" x="280" y="565" text-anchor="middle">ARGAN</text>
    <text class="product-type" x="280" y="752" text-anchor="middle">Oil</text>

    <text class="claim" x="280" y="805" text-anchor="middle">100% PURE AND ORGANIC</text>

    <path class="lower-band-line" d="M0,888 Q280,860 560,888" fill="none" stroke="var(--band-line)" stroke-width="4"/>
    <path class="lower-band" d="M0,896 Q280,868 560,896 L560,1040 L0,1040 Z" fill="var(--band-green)"/>

    <ellipse class="fruit-illustration" cx="278" cy="885" rx="118" ry="58" fill="url(#fruitGradient)" role="img" aria-label="Illustration of an argan branch with fruits and leaves"/>

    <text class="descriptor" x="280" y="985" text-anchor="middle">MOISTURING ESSENTIAL OIL</text>
    <text class="volume" x="280" y="1022" text-anchor="middle">4oz / 120ml</text>
  </svg>
</main>
</body>
</html>
```